Quenvo Festivals

We need a website that covers a website with reviews about different festivals all around the world. Should include a directory of festivals and artists as well as a nice overview of articles.

Should include
Homepage,
Directory over artists and a detail page for artists also linking them to
a directory over festivals and a detail page for each festival with different information boxes
A nice and clean article category view for possible use of sub categories from main article archive
A modern, clean and good article page

Target Market(s)

People from all over the world that travels to music festivals and enjoys to check information online and share good deals.

Industry/Entity Type

Festival

Requirements
Must have
• Review pages with boxes and spaces for information about festivals

```html
<!DOCTYPE html>
<html lang="en">
<head>
<meta charset="utf-8">
<title>Quenvo Festivals</title>
<link href="https://fonts.googleapis.com/css2?family=Open+Sans:wght@400;600;700;800&family=Oswald:wght@400;500&display=swap" rel="stylesheet">
<style>
:root{
  --orange:#f7941d;
  --orange-dark:#e27c0a;
  --ink:#333333;
  --muted:#777777;
  --page:#e6e6e6;
  --card:#ffffff;
  --nav:#4a4a4a;
  --nav-dark:#3a3a3a;
  --line:#d6d6d6;
  --green:#6a9b1f;
}
*{box-sizing:border-box;margin:0;padding:0}
html,body{width:1200px;height:2400px;overflow:hidden}
body{background:var(--page);font-family:"Open Sans",Arial,sans-serif;color:var(--ink);position:relative}
.abs{position:absolute}
/* header */
.site-header{left:0;top:0;width:1200px;height:112px;background:var(--card)}
.brand{left:26px;top:24px;display:flex;align-items:center;gap:14px}
.brand-mark{width:50px;height:50px;border-radius:50%;background:var(--orange)}
.brand-name{font-family:"Open Sans",sans-serif;font-weight:800;font-size:38px;color:var(--orange);letter-spacing:1px;white-space:nowrap}
.social{right:26px;top:36px;display:flex;gap:10px}
.social span{width:40px;height:40px;background:#8a8a8a;border-radius:4px}
.main-nav{left:0;top:112px;width:1200px;height:50px;background:var(--nav);border-bottom:3px solid var(--nav-dark)}
.main-nav ul{list-style:none;display:flex;height:100%}
.main-nav li{font-family:"Oswald",sans-serif;font-size:19px;color:#fff;text-transform:uppercase;padding:0 22px;line-height:48px;white-space:nowrap}
.main-nav li.active{background:var(--orange)}
.search{right:26px;top:10px;width:300px;height:30px;background:#2e2e2e;border-radius:3px;color:#aaa;font-size:15px;padding:5px 12px}
.search svg{position:absolute;right:10px;top:7px}
.hero{left:0;top:165px;width:1200px;height:440px;background:radial-gradient(ellipse at 60% 20%,#ffd46a 0%,#f28a1e 28%,#a2324a 60%,#2b1538 100%)}
/* cards */
.card{background:var(--card);box-shadow:0 1px 3px rgba(0,0,0,.12)}
.slider{left:20px;top:620px;width:720px;height:440px}
.slider-img{left:0;top:0;width:720px;height:390px;background:linear-gradient(180deg,#6b86a8 0%,#c9b9a6 45%,#7b5e4c 75%,#3a2c26 100%)}
.slider-cap{left:0;top:258px;width:720px;height:132px;background:rgba(0,0,0,.6);padding:16px 20px;color:#fff}
.slider-cap h2{font-size:28px;font-weight:700;white-space:nowrap}
.slider-cap p{font-size:15px;line-height:20px;margin-top:4px;color:#eee}
.slider-cap a{color:var(--orange);font-size:15px}
.dots{left:0;top:404px;width:720px;display:flex;justify-content:center;gap:10px}
.dots span{width:13px;height:13px;border-radius:50%;background:#bbb}
.dots span.on{background:#666}
.newsletter{left:772px;top:620px;width:408px;height:170px;padding:22px 24px}
.newsletter p{font-size:16px;line-height:22px;color:var(--muted)}
.nl-input{left:24px;top:100px;width:250px;height:40px;border:1px solid var(--line)}
.nl-btn{left:282px;top:100px;width:104px;height:40px;background:var(--orange);color:#fff;font-weight:700;font-size:14px;text-align:center;line-height:40px}
.offer{left:772px;top:805px;width:408px;height:255px;overflow:hidden}
.ribbon{left:-36px;top:36px;width:190px;height:40px;background:var(--orange);color:#fff;font-weight:700;font-size:13px;text-align:center;line-height:40px;transform:rotate(-40deg);white-space:nowrap}
.offer-big{left:170px;top:28px;font-size:50px;line-height:60px;font-weight:800;color:var(--orange);white-space:nowrap}
.offer-title{left:40px;top:122px;font-size:23px;line-height:30px;font-weight:700;white-space:nowrap}
.offer-text{left:40px;top:162px;width:340px;font-size:14px;line-height:19px;color:var(--muted)}
/* articles */
.article{left:20px;width:720px;height:360px;padding:24px 26px}
.article h2{font-size:30px;font-weight:700;line-height:38px}
.share{display:flex;gap:10px;margin-top:16px}
.share span{height:26px;padding:0 10px;border-radius:3px;background:#888;color:#fff;font-size:13px;font-weight:700;line-height:26px;display:flex;gap:8px}
.share span i{font-style:normal;background:#fff;color:#555;padding:0 6px;margin:3px 0;line-height:20px;border-radius:2px;font-weight:400}
.art-img{left:26px;top:150px;width:200px;height:150px}
.art-body{left:246px;top:152px;width:440px}
.art-meta{font-size:13px;color:#999}
.art-text{font-size:15px;line-height:21px;color:var(--muted);margin-top:8px}
.more{font-size:15px;color:var(--green);font-weight:600;margin-top:8px;display:block}
/* sidebar */
.tip{left:772px;top:1160px;width:408px;height:220px;background:#f2f2f2;padding:20px 24px;box-shadow:0 1px 3px rgba(0,0,0,.12)}
.tip h3{font-size:30px;font-weight:700}
.tip p{font-size:15px;line-height:21px;color:var(--muted);margin-top:10px}
.tip a{color:var(--orange);font-size:14px;display:block;margin-top:10px}
.upcoming{left:772px;top:1410px;width:408px}
.side-title{font-size:30px;font-weight:800;text-transform:uppercase;border-bottom:2px solid #999;padding-bottom:6px;white-space:nowrap}
.upcoming ul{list-style:none;margin-top:14px}
.upcoming li{font-size:17px;font-weight:700;line-height:32px;display:flex;align-items:center;gap:12px}
.upcoming li::before{content:"";width:14px;height:14px;background:var(--orange);border-radius:2px}
.archives{left:772px;top:1950px;width:408px;height:124px;padding:14px 20px}
.archives h3{font-size:30px;line-height:40px;font-weight:700}
.select{margin-top:12px;width:368px;height:40px;border:1px solid var(--line);font-size:15px;padding:8px 12px;position:relative}
.select::after{content:"";position:absolute;right:14px;top:15px;border:7px solid transparent;border-top-color:#555}
/* footer */
.footer-bar{left:0;top:2268px;width:1200px;height:36px;background:var(--card);border-top:1px solid var(--line);border-bottom:1px solid var(--line);padding:0 26px;display:flex;justify-content:space-between;align-items:center;font-size:14px;color:#555}
.footer-bar nav{display:flex;gap:22px}
.footer-note{left:0;top:2320px;width:1200px;text-align:center;font-size:14px;line-height:20px;color:#555}
.footer-note a{color:#3366aa}
</style>
</head>
<body>
<header class="abs site-header">
  <div class="abs brand"><span class="brand-mark"></span><span class="brand-name">Quenvo Festivals</span></div>
  <div class="abs social"><span></span><span></span><span></span><span></span></div>
</header>
<nav class="abs main-nav">
  <ul><li class="active">Home</li><li>About</li><li>Festivals</li><li>Artists</li><li>News</li><li>Tips</li><li>Contact Us</li></ul>
  <div class="abs search">search
    <svg width="16" height="16" viewBox="0 0 16 16"><circle cx="6.5" cy="6.5" r="5" fill="none" stroke="#ccc" stroke-width="2"/><line x1="10" y1="10" x2="15" y2="15" stroke="#ccc" stroke-width="2"/></svg>
  </div>
</nav>
<div class="abs hero" role="img" aria-label="Festival crowd with raised hands under warm stage lights"></div>

<section class="abs card slider">
  <div class="abs slider-img" role="img" aria-label="Outdoor festival crowd in front of a stage"></div>
  <div class="abs slider-cap">
    <h2>10 Unexpected Benefits Music Festivals</h2>
    <p>When buzzing phones and overflowing inboxes start to overwhelm, it's easier than you may think to take a break from technology. Read on for our best tips.</p>
    <a>Continue Reading »</a>
  </div>
  <div class="abs dots"><span class="on"></span><span></span><span></span><span></span><span></span></div>
</section>

<aside class="abs card newsletter">
  <p>Love what you're reading? Sign up for our newsletter and receive daily tips and inspiration!</p>
  <div class="abs nl-input"></div>
  <div class="abs nl-btn">SUBSCRIBE</div>
</aside>

<aside class="abs card offer">
  <div class="abs ribbon">LATEST EVENTS</div>
  <div class="abs offer-big">25% OFF!</div>
  <div class="abs offer-title">Name of Music Event Here</div>
  <p class="abs offer-text">Lorem ipsum dolor sit amet, consectetur adipiscing elit, sed do eiusmod tempor incididunt ut labore et dolore magna aliqua.</p>
</aside>

<article class="abs card article" style="top:1080px">
  <h2>The Social Media Festival Why I'm Going 30 Days Without Checking In</h2>
  <div class="share"><span>Share <i>2</i></span><span>Tweet <i>3</i></span><span>Save <i>0</i></span><span>+1 <i>0</i></span><span>Share <i>0</i></span></div>
  <div class="abs art-img" role="img" aria-label="Festival crowd photo" style="background:linear-gradient(160deg,#8fb0d6,#b99a7a 55%,#5b4438)"></div>
  <div class="abs art-body">
    <div class="art-meta">posted on Dec 11, 2013 | by Admin</div>
    <p class="art-text">When buzzing phones and overflowing inboxes start to overwhelm, it's easier than you may think to take a break from technology. Read on for our best tips.</p>
    <a class="more">Continue Reading »</a>
  </div>
</article>

<article class="abs card article" style="top:1460px">
  <h2>The Ultimate Guide to Dance Festivals</h2>
  <div class="share"><span>Share <i>2</i></span><span>Tweet <i>3</i></span><span>Save <i>0</i></span><span>+1 <i>0</i></span><span>Share <i>0</i></span></div>
  <div class="abs art-img" role="img" aria-label="Dancers at an evening festival" style="top:110px;background:linear-gradient(160deg,#3d5a8a,#8a6aa0 50%,#2a2333)"></div>
  <div class="abs art-body" style="top:112px">
    <div class="art-meta">posted on Dec 11, 2013 | by Admin</div>
    <p class="art-text">When buzzing phones and overflowing inboxes start to overwhelm, it's easier than you may think to take a break from technology. Read on for our best tips.</p>
    <a class="more">Continue Reading »</a>
  </div>
</article>

<article class="abs card article" style="top:1840px">
  <h2>10 Unexpected Benefits of Music Festivals</h2>
  <div class="share"><span>Share <i>2</i></span><span>Tweet <i>3</i></span><span>Save <i>0</i></span><span>+1 <i>0</i></span><span>Share <i>0</i></span></div>
  <div class="abs art-img" role="img" aria-label="Cheering crowd at a daytime festival" style="top:110px;background:linear-gradient(160deg,#e9b55c,#c5733a 50%,#4a2d22)"></div>
  <div class="abs art-body" style="top:112px">
    <div class="art-meta">posted on Dec 11, 2013 | by Admin</div>
    <p class="art-text">When buzzing phones and overflowing inboxes start to overwhelm, it's easier than you may think to take a break from technology. Read on for our best tips.</p>
    <a class="more">Continue Reading »</a>
  </div>
</article>

<aside class="abs tip">
  <h3>Tip of the Day!</h3>
  <p>In terms of health and price, farmed salmon can be a better bet than the wild stuff. Fish grown via aquaculture is lower in mercury and higher in B.</p>
  <a>read more »</a>
</aside>

<aside class="abs upcoming">
  <h3 class="side-title">Upcoming Festivals</h3>
  <ul>
    <li>Festival One</li><li>Australian Music Festival</li><li>Band Concert</li><li>Dance Music Competition</li><li>Festival Two</li><li>Open Stage Audition</li><li>Voice of the Coast Season 10</li><li>Dance Until Sunrise</li><li>Mini Mini Moh Event</li><li>Raise Your Hand</li><li>More Events</li>
  </ul>
</aside>

<aside class="abs card archives">
  <h3>Archives</h3>
  <div class="select">October 2013</div>
</aside>

<footer>
  <div class="abs footer-bar">
    <nav><span>Home</span><span>Events</span><span>Artists</span><span>FAQs</span><span>Terms &amp; Conditions</span><span>Privacy Policy</span></nav>
    <span>©2013 Quenvo Festivals. All rights reserved.</span>
  </div>
  <p class="abs footer-note">Disclaimer: Lorem ipsum dolor sit amet, consectetur adipiscing elit, sed do eiusmod tempor.<br>Questions? Email <a>hello@quenvofest.example</a> or Call 1 555 0142 718</p>
</footer>
</body>
</html>
```